Global Consulting firm needs a Business Card Design (Contest)

We need a business card design for a company with global reach called 'Hollowbrook Group'. Hollowbrook Group is a Trusted Procurement Advisor that consults for Pinnacle 400 and Meridel 900 companies to find cost reductions in their spending. We would like to see designs that communicate fiduciary trust and sense of partnership. The Front should have our logo w/ 'trusted procurement advisor', Employee name and title, company address, email, phone and fax (logo attached "Hollowbrook group final"). The color scheme and basic concept should be consistent with our presentation front page (attached "HBG presentation cover page"). The Back should have our website (www.hwbrookllc.com) and an array of our areas of expertise: office supplies, lab supplies, wireless telecom, MRO and IT (see "lab supplies" file for example).

```html
<!DOCTYPE html>
<html lang="en">
<head>
<meta charset="utf-8">
<title>Hollowbrook Group – Business Card</title>
<link rel="stylesheet" href="https://fonts.googleapis.com/css2?family=Crimson+Text:ital,wght@0,700;1,700&family=Jost:wght@400;500&display=swap">
<style>
  :root {
    --sheet: #c8c8c8;
    --charcoal: #333333;
    --paper: #ffffff;
    --copper: #a0654a;
    --ink: #2e2e2e;
    --gold: #e2bd1c;
    --label: #111111;
  }
  * { margin: 0; padding: 0; box-sizing: border-box; }
  html, body { width: 1200px; height: 456px; overflow: hidden; background: var(--sheet); }
  .sheet { position: relative; width: 1200px; height: 456px; font-family: "Jost", sans-serif; }

  .card { position: absolute; top: 81px; width: 512px; height: 299px; overflow: hidden; }
  .card--front { left: 39px; background: var(--charcoal); color: var(--paper); }
  .card--back { left: 640px; background: var(--paper); color: var(--ink); }

  .brand-mark { position: absolute; border-radius: 50%; background: var(--gold); }
  .card--front .brand-mark { left: 25px; top: 80px; width: 48px; height: 48px; }
  .card--back .brand-mark { left: 215px; top: 18px; width: 78px; height: 78px; }

  .brand-name {
    position: absolute; left: 89px; top: 88px;
    font-family: "Crimson Text", serif; font-weight: 700; font-size: 36px; line-height: 1;
    color: var(--paper); white-space: nowrap;
  }
  .tagline {
    position: absolute; left: 120px; top: 128px;
    font-family: "Crimson Text", serif; font-style: italic; font-weight: 700; font-size: 19px; line-height: 1;
    color: var(--paper); white-space: nowrap;
  }
  .rule { position: absolute; height: 7px; }
  .card--front .rule { left: 0; top: 159px; width: 480px; background: var(--paper); }
  .card--back .rule { left: 34px; top: 158px; width: 478px; height: 8px; background: var(--copper); }

  .person { position: absolute; left: 24px; top: 184px; }
  .contact { position: absolute; right: 32px; top: 184px; text-align: right; }
  .person p, .contact p { white-space: nowrap; line-height: 1; }
  .person__name, .contact__city { font-size: 17px; margin-bottom: 8px; }
  .person__title { font-size: 14px; color: var(--copper); margin-bottom: 8px; }
  .person__email { font-size: 13.5px; }
  .contact__line { font-size: 14px; margin-bottom: 7px; }
  .contact__label { color: var(--copper); }

  .website {
    position: absolute; left: 0; right: 0; top: 98px; text-align: center;
    font-size: 40px; line-height: 1; font-weight: 500; color: var(--ink); white-space: nowrap;
  }
  .website__accent { color: var(--copper); }
  .expertise { position: absolute; left: 0; right: 0; top: 173px; list-style: none; text-align: center; }
  .expertise li { font-size: 20px; line-height: 28px; color: var(--ink); }

  .side-label {
    position: absolute; top: 406px; width: 200px; text-align: center;
    font-size: 18px; line-height: 1; color: var(--label); letter-spacing: 0.5px;
  }
  .side-label--front { left: 195px; }
  .side-label--back { left: 796px; }
</style>
</head>
<body>
<main class="sheet">
  <section class="card card--front" aria-label="Card front">
    <span class="brand-mark"></span>
    <h1 class="brand-name">Hollowbrook Group</h1>
    <p class="tagline">Trusted Procurement Advisor</p>
    <div class="rule"></div>
    <div class="person">
      <p class="person__name">Daniel Reyes</p>
      <p class="person__title">President</p>
      <p class="person__email">danielreyes@hwbrookllc.com</p>
    </div>
    <div class="contact">
      <p class="contact__city">Cedar Hollow, New Jersey</p>
      <p class="contact__line"><span class="contact__label">Phone:</span> (866) 555 – 0142</p>
      <p class="contact__line"><span class="contact__label">Fax:</span> (609) 555 – 0187</p>
      <p class="contact__line"><span class="contact__label">E-Mail:</span> info@hwbrookllc.com</p>
    </div>
  </section>

  <section class="card card--back" aria-label="Card back">
    <span class="brand-mark"></span>
    <p class="website"><span class="website__accent">www.</span>hwbrookllc<span class="website__accent">.com</span></p>
    <div class="rule"></div>
    <ul class="expertise">
      <li>Office supplies</li>
      <li>Lab supplies</li>
      <li>Wireless telecom</li>
      <li>MRO and IT</li>
    </ul>
  </section>

  <p class="side-label side-label--front">FRONT</p>
  <p class="side-label side-label--back">BACK</p>
</main>
</body>
</html>
```